I need a very simple poster with the following quote:
"Cada escolha, uma renĂșncia, isso Ă© a vida"
Which means that to every choice there is a waiver, that's life.

It will be framed and used in my living room.

The poster has to be black and white. It is not mandatory to use commas and quotes.

The design has to be modern, like the references I posted on this board: http://pinboardly.example/marvetu/ideas/

```html
<!DOCTYPE html>
<html lang="pt">
<head>
<meta charset="utf-8">
<title>Cada escolha uma renúncia — isso é a vida</title>
<link rel="stylesheet" href="https://fonts.googleapis.com/css2?family=Roboto+Condensed:wght@900&display=swap">
<style>
  :root {
    --ink: #000000;
    --paper: #ffffff;
  }
  html, body {
    margin: 0;
    padding: 0;
    width: 849px;
    height: 1200px;
    overflow: hidden;
    background: var(--ink);
  }
  .poster {
    display: block;
    width: 849px;
    height: 1200px;
  }
  .poster__ground { fill: var(--ink); }
  .poster__banner { fill: var(--paper); }
  .quote {
    font-family: "Roboto Condensed", "Arial Narrow", sans-serif;
    font-weight: 900;
    text-transform: uppercase;
  }
  .quote--light { fill: var(--paper); }
  .quote--dark { fill: var(--ink); }
</style>
</head>
<body>
<svg class="poster" viewBox="0 0 849 1200" xmlns="http://www.w3.org/2000/svg" role="img" aria-label="Cada escolha uma renúncia, isso é a vida">
  <rect class="poster__ground" width="849" height="1200"/>
  <polygon class="poster__banner" points="108,393 741,212 741,818 291,989 291,777 108,777"/>

  <text class="quote quote--light quote__cada" x="62" y="282" font-size="205"
        textLength="470" lengthAdjust="spacingAndGlyphs"
        transform="rotate(-17 62 282)">Cada</text>
  <text class="quote quote--light quote__escolha" x="120" y="378" font-size="122"
        textLength="440" lengthAdjust="spacingAndGlyphs"
        transform="rotate(-17 120 378)">Escolha</text>

  <text class="quote quote--dark quote__uma" x="213" y="560" font-size="200"
        textLength="434" lengthAdjust="spacingAndGlyphs">Uma</text>
  <text class="quote quote--dark quote__renuncia" x="144" y="698" font-size="137"
        textLength="566" lengthAdjust="spacingAndGlyphs">Renuncia</text>

  <text class="quote quote--light quote__isso" x="108" y="857" font-size="94"
        textLength="169" lengthAdjust="spacingAndGlyphs">Isso</text>
  <text class="quote quote--light quote__e-a" x="108" y="988" font-size="94"
        textLength="172" lengthAdjust="spacingAndGlyphs">É A</text>

  <text class="quote quote--light quote__vida" x="308" y="1160" font-size="255"
        textLength="520" lengthAdjust="spacingAndGlyphs"
        transform="rotate(-20 308 1160)">Vida</text>
</svg>
</body>
</html>
```